Relocation/furniture installation company needs new business cards

we are a relocation and furniture installation company mainly dealing with corporate clients and we are looking for new business card ideas. Cards should incorporate our logo and list our website, phone number and services. The company is only 2 years old but with more staff joining we are in the need for more business cards, so something with an awesome design that is eye catching would go a long way to insure we get our name out there and look good to potential new clients.

Target Market(s)

Corporate

Industry/Entity Type

Trade

Contact Information for Business Card

www.mervoline.co.nz
0508 4 bravok

furniture installation
business relocations
joinery installation
commercial property maintenance

Colors
0592cd
34a7d8
85cae6
85acd3
0356a4
cfdfed
cee9f5
757575
474747

Requirements
Must have
• Business relocations and furniture installation specialists
Nice to have
• something that incorporates our logo.

```html
<!DOCTYPE html>
<html lang="en">
<head>
<meta charset="UTF-8">
<title>Mervoline Business Cards</title>
<link rel="stylesheet" href="https://fonts.googleapis.com/css2?family=Open+Sans:wght@400;600&display=swap">
<style>
  :root {
    --bg: #ececec;
    --card: #ffffff;
    --brand-deep: #0356a4;
    --brand-blue: #0592cd;
    --band: #474747;
    --muted: #757575;
    --text-dark: #333333;
  }
  * { box-sizing: border-box; margin: 0; padding: 0; }
  html, body { width: 1200px; height: 800px; overflow: hidden; }
  body {
    background: var(--bg);
    font-family: "Open Sans", sans-serif;
    position: relative;
  }
  .card {
    position: absolute;
    top: 252px;
    width: 520px;
    height: 297px;
    background: var(--card);
    box-shadow: 0 2px 6px rgba(0,0,0,0.12);
  }
  .card--front { left: 50px; }
  .card--back { left: 630px; }

  /* Front */
  .front-mark {
    position: absolute;
    inset: 0;
    display: flex;
    align-items: center;
    justify-content: center;
    gap: 18px;
  }
  .front-mark__square {
    width: 44px; height: 44px;
    background: var(--brand-blue);
  }
  .front-mark__name {
    font-size: 50px;
    font-weight: 600;
    letter-spacing: 6px;
    color: var(--brand-deep);
  }

  /* Back */
  .back-mark {
    position: absolute;
    left: 40px; top: 58px;
    display: flex; align-items: center; gap: 8px;
  }
  .back-mark__square { width: 16px; height: 16px; background: var(--brand-blue); }
  .back-mark__name {
    font-size: 17px; font-weight: 600; letter-spacing: 2px;
    color: var(--brand-deep);
  }
  .details {
    position: absolute;
    left: 250px; top: 40px; width: 240px;
  }
  .details__name {
    font-size: 20px; font-weight: 400;
    color: var(--brand-blue);
    letter-spacing: 1px;
    padding-bottom: 4px;
    border-bottom: 1px solid var(--band);
    margin-bottom: 10px;
  }
  .contact-row {
    display: flex; align-items: center; gap: 8px;
    font-size: 11px; color: var(--text-dark);
    margin-bottom: 6px;
  }
  .contact-row svg { width: 18px; height: 18px; flex: none; }
  .services {
    margin-top: 6px;
    font-size: 11px; line-height: 1.4;
    color: var(--brand-blue);
  }
  .tagline-band {
    position: absolute;
    left: 0; right: 0; top: 196px;
    height: 30px;
    background: var(--band);
    color: #ffffff;
    font-size: 11px;
    letter-spacing: 0.5px;
    display: flex; align-items: center;
    padding-left: 40px;
    text-transform: uppercase;
  }
</style>
</head>
<body>
  <section class="card card--front" aria-label="Card front">
    <div class="front-mark">
      <span class="front-mark__square"></span>
      <span class="front-mark__name">MERVOLINE</span>
    </div>
  </section>

  <section class="card card--back" aria-label="Card back">
    <div class="back-mark">
      <span class="back-mark__square"></span>
      <span class="back-mark__name">MERVOLINE</span>
    </div>

    <div class="details">
      <h2 class="details__name">MERVOLINE</h2>
      <div class="contact-row">
        <svg viewBox="0 0 20 20" aria-hidden="true">
          <circle cx="10" cy="10" r="10" fill="#757575"/>
          <circle cx="10" cy="10" r="5.5" fill="none" stroke="#fff" stroke-width="1"/>
          <ellipse cx="10" cy="10" rx="2.4" ry="5.5" fill="none" stroke="#fff" stroke-width="1"/>
          <line x1="4.5" y1="10" x2="15.5" y2="10" stroke="#fff" stroke-width="1"/>
        </svg>
        <span>www.mervoline.co.nz</span>
      </div>
      <div class="contact-row">
        <svg viewBox="0 0 20 20" aria-hidden="true">
          <circle cx="10" cy="10" r="10" fill="#474747"/>
          <path d="M7.2 5.5c.5-.4 1.1-.2 1.4.3l.8 1.5c.2.4.1.9-.3 1.2l-.6.4c.4 1.2 1.3 2.2 2.5 2.7l.4-.6c.3-.4.8-.5 1.2-.3l1.5.8c.5.3.6.9.3 1.4l-.6.8c-.5.6-1.3.8-2 .5-2.6-1-4.6-3-5.5-5.6-.2-.7 0-1.5.6-2z" fill="#fff"/>
        </svg>
        <span>0508 4 bravok</span>
      </div>
      <p class="services">
        furniture installation | business relocations<br>
        joinery installation |<br>
        commercial property maintenance
      </p>
    </div>

    <div class="tagline-band">Business relocations and furniture installation specialists</div>
  </section>
</body>
</html>
```